Gearloft forum banner

Need a banner ad for a forum relating to the motor car industry.
I have attached a sample banner , we need ours to be edited to suit our web site - gearloft-example.com.au
Image needs to be roughly 400px by 100px.
We would like to display information like the pic below named kelbanner but with a better design / colour / image combination.

```html
<!DOCTYPE html>
<html lang="en">
<head>
<meta charset="utf-8">
<title>Gearloft – Japan Car Import Service</title>
<link href="https://fonts.googleapis.com/css2?family=Arimo:wght@400;700&display=swap" rel="stylesheet">
<style>
  :root {
    --bg-dark: #141414;
    --bg-mid: #2a2a2a;
    --red: #e0141e;
    --red-dark: #b30c14;
    --white: #ffffff;
    --text-soft: #e6e6e6;
    --panel: rgba(10, 10, 10, 0.82);
    --panel-edge: #4a4a4a;
    --car-light: #e9ecef;
    --car-shade: #8a9098;
  }
  * { margin: 0; padding: 0; box-sizing: border-box; }
  html, body {
    width: 1200px; height: 400px; overflow: hidden;
    background: var(--bg-dark);
  }
  .banner {
    position: relative;
    width: 1200px; height: 400px;
    overflow: hidden;
    font-family: "Arimo", Arial, sans-serif;
    color: var(--white);
    background: radial-gradient(ellipse at 40% 40%, var(--bg-mid) 0%, var(--bg-dark) 75%);
  }
  .vehicle-photo {
    position: absolute;
    left: 560px; top: 80px;
    width: 640px; height: 320px;
    background: radial-gradient(ellipse at 55% 55%, var(--car-light) 0%, #c4c9cf 45%, var(--car-shade) 70%, rgba(20,20,20,0) 100%);
  }
  .headline {
    position: absolute;
    left: 22px; top: 14px;
    font-size: 42px; font-weight: 700;
    letter-spacing: 0.5px;
    line-height: 1;
  }
  .headline .accent { color: var(--red); }
  .tagline {
    position: absolute;
    left: 24px; top: 70px;
    font-size: 31px; font-weight: 400;
    color: var(--text-soft);
  }
  .services {
    position: absolute;
    left: 20px; top: 140px;
    width: 580px; height: 175px;
    background: var(--panel);
    border: 2px solid var(--panel-edge);
    border-radius: 8px;
    padding: 22px 22px;
    list-style: none;
    display: flex; flex-wrap: wrap;
    align-content: space-between;
    column-gap: 22px;
  }
  .services li {
    display: flex; align-items: center;
    font-size: 34px; line-height: 1;
    color: var(--white);
  }
  .services li::before {
    content: "";
    width: 14px; height: 14px;
    background: var(--red);
    margin-right: 10px;
  }
  .services li.etc::before { display: none; }
  .services li.etc { color: var(--red); margin-left: 4px; }
  .brand {
    position: absolute;
    left: 26px; top: 328px;
    display: flex; align-items: center; gap: 14px;
    font-size: 44px; font-weight: 700;
    color: var(--white);
  }
  .brand .mark {
    width: 28px; height: 28px;
    background: var(--red);
  }
  .cta {
    position: absolute;
    left: 900px; top: 320px;
    width: 274px; height: 66px;
    background: linear-gradient(var(--red) 0%, var(--red-dark) 100%);
    border: 2px solid #ff5a60;
    border-radius: 4px;
    display: flex; align-items: center; justify-content: center;
    font-size: 34px; font-weight: 700;
    color: var(--white);
    letter-spacing: 0.5px;
  }
</style>
</head>
<body>
  <div class="banner">
    <div class="vehicle-photo" role="img" aria-label="White Japanese sedan seen from the front three-quarter angle"></div>

    <h1 class="headline">JAPAN CAR IMPORT <span class="accent">SERVICE</span></h1>
    <p class="tagline">We Arrange Everything For You</p>

    <ul class="services">
      <li>Vehicle purchase</li>
      <li>Shipping</li>
      <li>Customs</li>
      <li>Compliance</li>
      <li>Registration</li>
      <li class="etc">ETC.</li>
    </ul>

    <div class="brand"><span class="mark"></span>Gearloft</div>

    <div class="cta">LEARN MORE</div>
  </div>
</body>
</html>
```